Business Card Design

This is a new business to be run from my home. I have attended certificate workshops run by Dr Derek Onwu who is a Master Trainer in Harbor Steps Method.
I wish to communicate to people that Tai Chi is for everyone, no matter their age, gender or fitness levels. Tai Chi is taught both standing & seated.
The card should have a slightly Asian feel, mainly printed in black & white with perhaps a little soft pink &/or green.

Target Market(s)

people of all ages from 10 years up, poor fitness & mild disabilities.

Industry/Entity Type

Fitness

Contact Information for Business Card

Wexmoor Tai Chi for Fitness, Health & Relaxation

Branna Holt, Certificated Leader

ph 4091 5528

Requirements
Nice to have
• a feeling of health & peace.
Should not have
• bright colours, fancy fonts

```html
<!DOCTYPE html>
<html lang="en">
<head>
<meta charset="utf-8">
<title>Wexmoor Tai Chi – Business Card</title>
<link rel="stylesheet" href="https://fonts.googleapis.com/css2?family=Comfortaa:wght@500&family=Poiret+One&display=swap">
<style>
  :root {
    --card-bg: #ffffff;
    --ink: #111111;
    --lilac: #d8c3e8;
    --lilac-soft: #efe6f5;
  }
  html, body {
    margin: 0;
    padding: 0;
    width: 1200px;
    height: 741px;
    overflow: hidden;
    background: var(--card-bg);
  }
  .card {
    position: relative;
    width: 1200px;
    height: 741px;
    background: var(--card-bg);
    overflow: hidden;
    color: var(--ink);
  }
  .floral-panel {
    position: absolute;
    left: 0;
    top: 0;
    width: 440px;
    height: 741px;
    background:
      radial-gradient(ellipse at 30% 35%, var(--lilac) 0%, var(--lilac-soft) 45%, rgba(255,255,255,0) 75%),
      linear-gradient(90deg, var(--lilac-soft) 0%, rgba(255,255,255,0) 100%);
  }
  .details {
    position: absolute;
    right: 71px;
    top: 0;
    text-align: right;
  }
  .business-name {
    position: absolute;
    right: 0;
    top: 80px;
    margin: 0;
    white-space: nowrap;
    font-family: "Comfortaa", sans-serif;
    font-weight: 500;
    font-size: 78px;
    line-height: 1;
    letter-spacing: -1px;
  }
  .tagline {
    position: absolute;
    right: 0;
    top: 188px;
    margin: 0;
    white-space: nowrap;
    font-family: "Poiret One", sans-serif;
    font-size: 44px;
    line-height: 1;
  }
  .leader-name {
    position: absolute;
    right: 0;
    top: 355px;
    margin: 0;
    white-space: nowrap;
    font-family: "Comfortaa", sans-serif;
    font-weight: 500;
    font-size: 72px;
    line-height: 1;
    letter-spacing: -1px;
  }
  .leader-role {
    position: absolute;
    right: 0;
    top: 458px;
    margin: 0;
    white-space: nowrap;
    font-family: "Poiret One", sans-serif;
    font-size: 52px;
    line-height: 1;
  }
  .phone {
    position: absolute;
    right: 0;
    top: 610px;
    margin: 0;
    white-space: nowrap;
    font-family: "Poiret One", sans-serif;
    font-size: 42px;
    line-height: 1;
    letter-spacing: 1px;
  }
</style>
</head>
<body>
  <div class="card">
    <div class="floral-panel" role="img" aria-label="Black swirling floral vine ornament with lilac shadow, flowers and spirals running down the left edge"></div>
    <div class="details">
      <h1 class="business-name">Wexmoor Tai Chi</h1>
      <p class="tagline">for Fitness, Health &amp; Relaxation</p>
      <h2 class="leader-name">Branna Holt</h2>
      <p class="leader-role">Certified Leader</p>
      <p class="phone">ph 4091 5528</p>
    </div>
  </div>
</body>
</html>
```